Occupational Therapist does home accessibility for disabled folks; needs business card design

We need a business card for a company in Portland, Oregon that specializes in making homes accessible, comfortable, and functional for people who are disabled or aging who would like to stay in THEIR home. Our medical background as Occupational Therapists allows us to translate the functional needs of the person into the recommendations for the design of the home remodel.

Target Market(s)

Elderly, children of elderly
People with disabilities, families of people with disabilities

Industry/Entity Type

Business

Contact Information for Business Card

Company name: HomeWise
Name: Danielle Reyes Crawford, OTR/L, CAPS, ECHM
Occupational Therapist, Home Modification & Accessibility Specialist
website: www.homewiseforyears.com
email: homewiseforyears@nestmail.example
phone: (503)218-4057
CCB #: 487315

Font styles to use
Sans Serif

Requirements
Must have
• My logo
• Easy to read font with contrasting background
• Please list the Services offered: Occupational Therapy, Home safety & accessibility assessments, Home modification consulting, project management
Nice to have
• Friendly, welcoming feel
Should not have
• Dark colored background

```html
<!DOCTYPE html>
<html lang="en">
<head>
<meta charset="UTF-8">
<title>HomeWise Business Card</title>
<link href="https://fonts.googleapis.com/css2?family=Lato:wght@400;700&display=swap" rel="stylesheet">
<style>
  :root {
    --page-bg: #ecebe8;
    --card-white: #ffffff;
    --charcoal: #4b4b4d;
    --orange: #c8711f;
    --text: #3f3f41;
  }
  * { margin: 0; padding: 0; box-sizing: border-box; }
  html, body {
    width: 1138px; height: 1200px; overflow: hidden;
    background: var(--page-bg);
    font-family: "Lato", sans-serif;
    color: var(--text);
  }
  .card {
    position: absolute;
    width: 670px; height: 383px;
    box-shadow: 0 4px 14px rgba(0,0,0,0.18);
    overflow: hidden;
  }
  /* Front */
  .card-front { left: 218px; top: 198px; background: var(--card-white); }
  .brand {
    position: absolute; left: 46px; top: 166px;
    display: flex; align-items: center; gap: 11px;
  }
  .brand-square { width: 24px; height: 24px; background: var(--orange); flex: none; }
  .brand-name {
    font-weight: 700; font-size: 36px; letter-spacing: 0.3px;
    color: var(--charcoal); white-space: nowrap;
  }
  .divider {
    position: absolute; left: 292px; top: 94px;
    width: 1px; height: 198px; background: var(--orange);
  }
  .contact { position: absolute; left: 308px; right: 28px; top: 96px; }
  .person-name { font-weight: 700; font-size: 21px; color: var(--orange); line-height: 1.2; }
  .credentials { font-size: 15.5px; line-height: 19px; }
  .contact-list { list-style: none; margin-top: 14px; }
  .contact-list li {
    display: flex; align-items: center; gap: 6px;
    font-size: 18px; line-height: 24px; white-space: nowrap;
  }
  .contact-list svg { width: 16px; height: 16px; flex: none; }
  .ccb { font-size: 15.5px; line-height: 20px; }

  /* Back */
  .card-back { left: 216px; top: 617px; background: var(--charcoal); }
  .back-brand {
    position: absolute; left: 0; right: 0; top: 108px;
    display: flex; justify-content: center; align-items: center; gap: 16px;
  }
  .back-brand .brand-square { width: 36px; height: 36px; }
  .back-brand .brand-name { font-size: 58px; color: #ffffff; }
  .services-band {
    position: absolute; left: 0; right: 0; top: 288px; height: 71px;
    background: var(--card-white);
    text-align: center; padding-top: 7px;
  }
  .services-title { font-size: 16px; color: var(--orange); line-height: 20px; }
  .services-list { font-size: 15.5px; line-height: 20px; }
</style>
</head>
<body>
  <section class="card card-front">
    <div class="brand">
      <span class="brand-square"></span>
      <span class="brand-name">HomeWise</span>
    </div>
    <div class="divider"></div>
    <div class="contact">
      <p class="person-name">Danielle Reyes Crawford</p>
      <p class="credentials">OTR/L, CAPS, ECHM<br>Occupational Therapist<br>Home Modification &amp; Accessibility Specialist</p>
      <ul class="contact-list">
        <li>
          <svg viewBox="0 0 16 16" aria-hidden="true"><path d="M4 1.5 L6.5 4.5 L5 6.5 Q6.5 9.5 9.5 11 L11.5 9.5 L14.5 12 L12.5 14.5 Q6 14 1.5 4 Z" fill="var(--orange)"/></svg>
          (503) 218-4057
        </li>
        <li>
          <svg viewBox="0 0 16 16" aria-hidden="true"><rect x="1" y="3" width="14" height="10" fill="var(--orange)"/><path d="M1 3 L8 9 L15 3" stroke="#fff" stroke-width="1.2" fill="none"/></svg>
          homewiseforyears@nestmail.example
        </li>
        <li>
          <svg viewBox="0 0 16 16" aria-hidden="true"><g fill="none" stroke="var(--orange)" stroke-width="1.3"><circle cx="8" cy="8" r="6.5"/><ellipse cx="8" cy="8" rx="3" ry="6.5"/><line x1="1.5" y1="8" x2="14.5" y2="8"/></g></svg>
          www.homewiseforyears.com
        </li>
      </ul>
      <p class="ccb">CCB #: 487315</p>
    </div>
  </section>

  <section class="card card-back">
    <div class="back-brand">
      <span class="brand-square"></span>
      <span class="brand-name">HomeWise</span>
    </div>
    <div class="services-band">
      <p class="services-title">Services we provide:</p>
      <p class="services-list">Occupational Therapy, Home safety &amp; accessibility assessments<br>Home modification consulting, Project management</p>
    </div>
  </section>
</body>
</html>
```